Van wrap for landscaping business

I have a logo by you guys. I want to put the logo and add a couple of words and a picture of something compelling, maybe a picture of a nice grassy yard. I want the words Residential, Commercial, Clean Ups, and Haul Aways on the wrap. I have a Kolbrand Traveller van with a high roof 170 in length. I attached a picture of the van. I would like to wrap just the rear of the van, everything except the cabin. Can you help me with this project?

Target Market(s)

Advertise my business

Industry/Entity Type

Landscaping

Requirements
Must have
• My logo, the words : Residential, Commercial, Clean Ups, and Haul Aways
Nice to have
• A picture or drawing of a nice dark green grass field or yard.

```html
<!DOCTYPE html>
<html lang="en">
<head>
<meta charset="utf-8">
<title>Verdell Landscaping – Van Wrap</title>
<link href="https://fonts.googleapis.com/css2?family=Rubik:wght@700;800&family=Play:wght@700&display=swap" rel="stylesheet">
<style>
  :root {
    --page: #ffffff;
    --forest: #0f2a0c;
    --forest-deep: #0a1f08;
    --band: #1d211d;
    --white: #ffffff;
    --outline: #c9cec9;
    --glass: #3a3f3a;
    --sky: #bfe3ee;
    --grass-light: #9fd27a;
    --grass: #4f9a3c;
    --grass-dark: #24511b;
    --ink: #1a3a16;
    --accent: #e6b820;
    --rear-black: #060806;
  }
  html, body {
    margin: 0;
    padding: 0;
    width: 879px;
    height: 1200px;
    overflow: hidden;
    background: var(--page);
  }
  .wrap-sheet { display: block; width: 879px; height: 1200px; }
  .services { font-family: "Rubik", sans-serif; font-weight: 800; fill: var(--white); }
  .divider { fill: var(--accent); }
  .phone { font-family: "Rubik", sans-serif; font-weight: 700; fill: var(--white); }
  .web { font-family: "Rubik", sans-serif; font-weight: 700; fill: var(--white); }
  .brand-name { font-family: "Play", sans-serif; font-weight: 700; fill: var(--ink); letter-spacing: 1.5px; }
  .brand-phone { font-family: "Play", sans-serif; font-weight: 700; fill: var(--ink); letter-spacing: 1px; }
  .bullet { fill: var(--accent); }
  .body-outline { fill: none; stroke: var(--outline); stroke-width: 1.5; }
  .scene-ring { fill: none; stroke: var(--forest-deep); stroke-width: 2; }
</style>
</head>
<body>
<svg class="wrap-sheet" viewBox="0 0 879 1200" xmlns="http://www.w3.org/2000/svg">
  <defs>
    <linearGradient id="lawn-scene" x1="0" y1="0" x2="0" y2="1">
      <stop offset="0" stop-color="var(--sky)"/>
      <stop offset="0.42" stop-color="#d8eef2"/>
      <stop offset="0.52" stop-color="var(--grass-light)"/>
      <stop offset="0.66" stop-color="var(--grass)"/>
      <stop offset="0.8" stop-color="var(--grass-dark)"/>
      <stop offset="1" stop-color="var(--forest)"/>
    </linearGradient>
    <linearGradient id="badge-scene" x1="0" y1="0" x2="0" y2="1">
      <stop offset="0" stop-color="var(--sky)"/>
      <stop offset="0.55" stop-color="var(--grass-light)"/>
      <stop offset="1" stop-color="var(--grass)"/>
    </linearGradient>
    <path id="side-body" d="M0,245 L0,188 Q0,162 18,152 L168,10 Q176,3 196,3 L700,3 Q714,3 714,17 L714,245 L603,245 A46,46 0 0 0 511,245 L142,245 A46,46 0 0 0 50,245 Z"/>
    <path id="rear-body" d="M8,380 L4,140 C6,40 30,4 80,2 L251,2 C301,4 325,40 327,140 L323,380 Q323,393 310,393 L21,393 Q8,393 8,380 Z"/>
    <path id="front-body" d="M30,420 L22,170 Q20,60 60,20 Q80,2 120,2 L232,2 Q272,2 292,20 Q332,60 330,170 L322,420 Z"/>
    <clipPath id="side-clip"><use href="#side-body"/></clipPath>
    <clipPath id="rear-clip"><use href="#rear-body"/></clipPath>
  </defs>

  <!-- Driver side -->
  <g class="side-panel side-panel--left" transform="translate(116,77)">
    <g clip-path="url(#side-clip)">
      <rect class="cab-white" width="714" height="245" fill="var(--white)"/>
      <path class="cab-window" d="M40,150 L150,45 L212,42 Q220,42 220,50 L220,112 L120,118 Z" fill="var(--glass)"/>
      <path class="body-green" d="M0,245 L0,205 C40,170 110,140 180,140 C240,140 270,190 324,190 C380,190 400,150 410,0 L714,0 L714,245 Z" fill="var(--forest)"/>
      <g class="lawn-scene" role="img" aria-label="Illustration of a lawn mower on a green grassy yard under a sunny sky">
        <circle cx="553" cy="142" r="137" fill="url(#lawn-scene)"/>
      </g>
      <rect class="rocker-band" x="0" y="192" width="714" height="24" fill="var(--band)"/>
      <rect class="sill" x="0" y="216" width="714" height="29" fill="var(--forest-deep)"/>
      <circle class="logo-disc" cx="324" cy="99" r="92" fill="var(--white)"/>
    </g>
    <use href="#side-body" class="body-outline"/>
    <g class="brand-mark">
      <circle cx="324" cy="60" r="33" fill="url(#badge-scene)" role="img" aria-label="Badge with a lawn mower on grass"/>
      <text class="brand-name" x="324" y="112" font-size="12.5" text-anchor="middle">VERDELL LANDSCAPING</text>
      <text class="brand-phone" x="324" y="136" font-size="11" text-anchor="middle">(555) 014-2290</text>
    </g>
    <text class="phone" x="173" y="171" font-size="12.5" text-anchor="middle">555 0198 576</text>
    <text class="services" x="557" y="164" font-size="16.5" text-anchor="middle">Clean Ups <tspan class="divider">|</tspan> Haul Aways</text>
    <text class="services" x="557" y="181" font-size="16.5" text-anchor="middle">Residential <tspan class="divider">|</tspan> Commercial</text>
    <text class="web" x="377" y="236" font-size="15.5" text-anchor="middle">VerdellLandscaping.com</text>
  </g>

  <!-- Front -->
  <g class="front-panel" transform="translate(85,404)">
    <use href="#front-body" fill="var(--white)" stroke="var(--outline)" stroke-width="1.5"/>
    <path class="windshield" d="M52,70 Q56,58 70,58 L282,58 Q296,58 300,70 L312,150 L40,150 Z" fill="var(--glass)" opacity="0.85"/>
    <rect class="front-bumper" x="36" y="290" width="280" height="70" rx="10" fill="var(--band)"/>
    <g class="brand-mark brand-mark--hood">
      <circle cx="176" cy="186" r="22" fill="url(#badge-scene)" role="img" aria-label="Badge with a lawn mower on grass"/>
      <text class="brand-name" x="176" y="216" font-size="7.5" text-anchor="middle">VERDELL LANDSCAPING</text>
      <text class="brand-phone" x="176" y="229" font-size="6.5" text-anchor="middle">(555) 014-2290</text>
    </g>
  </g>

  <!-- Rear -->
  <g class="rear-panel" transform="translate(490,405)">
    <g clip-path="url(#rear-clip)">
      <rect width="331" height="395" fill="var(--rear-black)"/>
      <rect class="rear-white" x="73" y="0" width="187" height="120" fill="var(--white)"/>
      <path class="lawn-scene" role="img" aria-label="Illustration of a lawn mower on a green grassy yard under a sunny sky"
            d="M22,242 L22,200 C22,150 70,120 166,120 C262,120 310,150 310,200 L310,242 Z" fill="url(#lawn-scene)"/>
      <circle class="logo-disc" cx="166" cy="74" r="88" fill="var(--white)"/>
      <rect class="rear-bumper" x="0" y="340" width="331" height="55" fill="#141714"/>
    </g>
    <use href="#rear-body" class="body-outline"/>
    <g class="brand-mark">
      <circle cx="166" cy="42" r="29" fill="url(#badge-scene)" role="img" aria-label="Badge with a lawn mower on grass"/>
      <text class="brand-name" x="166" y="92" font-size="11" text-anchor="middle">VERDELL LANDSCAPING</text>
      <text class="brand-phone" x="166" y="114" font-size="10" text-anchor="middle">(555) 014-2290</text>
    </g>
    <circle class="bullet" cx="56" cy="256" r="2"/>
    <text class="services" x="62" y="260" font-size="12.5">Clean Ups</text>
    <circle class="bullet" cx="56" cy="270" r="2"/>
    <text class="services" x="62" y="274" font-size="12.5">Haul Aways</text>
    <circle class="bullet" cx="190" cy="256" r="2"/>
    <text class="services" x="196" y="260" font-size="12.5">Residential</text>
    <circle class="bullet" cx="190" cy="270" r="2"/>
    <text class="services" x="196" y="274" font-size="12.5">Commercial</text>
    <text class="phone" x="239" y="302" font-size="16.5" text-anchor="middle">555 0198 576</text>
    <text class="web" x="239" y="315" font-size="8" text-anchor="middle">VerdellLandscaping.com</text>
  </g>

  <!-- Passenger side -->
  <g class="side-panel side-panel--right" transform="translate(48,877)">
    <g transform="translate(714,0) scale(-1,1)">
      <g clip-path="url(#side-clip)">
        <rect width="714" height="245" fill="var(--white)"/>
        <path class="cab-window" d="M40,150 L150,45 L212,42 Q220,42 220,50 L220,112 L120,118 Z" fill="var(--glass)"/>
        <path class="body-green" d="M0,245 L0,205 C40,170 110,140 180,140 C240,140 270,190 324,190 C380,190 400,150 410,0 L714,0 L714,245 Z" fill="var(--forest)"/>
        <g class="lawn-scene" role="img" aria-label="Illustration of a lawn mower on a green grassy yard under a sunny sky">
          <circle cx="551" cy="140" r="139" fill="url(#lawn-scene)"/>
        </g>
        <rect x="0" y="192" width="714" height="24" fill="var(--band)"/>
        <rect x="0" y="216" width="714" height="29" fill="var(--forest-deep)"/>
        <circle class="logo-disc" cx="322" cy="97" r="92" fill="var(--white)"/>
      </g>
      <use href="#side-body" class="body-outline"/>
    </g>
    <g class="brand-mark">
      <circle cx="392" cy="58" r="33" fill="url(#badge-scene)" role="img" aria-label="Badge with a lawn mower on grass"/>
      <text class="brand-name" x="392" y="110" font-size="12.5" text-anchor="middle">VERDELL LANDSCAPING</text>
      <text class="brand-phone" x="392" y="134" font-size="11" text-anchor="middle">(555) 014-2290</text>
    </g>
    <text class="services" x="163" y="164" font-size="16.5" text-anchor="middle">Clean Ups <tspan class="divider">|</tspan> Haul Aways</text>
    <text class="services" x="163" y="181" font-size="16.5" text-anchor="middle">Residential <tspan class="divider">|</tspan> Commercial</text>
    <text class="phone" x="541" y="171" font-size="12.5" text-anchor="middle">555 0198 576</text>
    <text class="web" x="338" y="236" font-size="15.5" text-anchor="middle">VerdellLandscaping.com</text>
  </g>
</svg>
</body>
</html>
```